Medical Billing Company Needs a Business Card Design

We need a business card design for a Florida based medical billing company called 'Lorrimer Tallbrook Services'. We specialize in providing revenue cycle management services to physician and therapist offices (we're basically their back-office processing partner for providing billing software, claims submissions, A/R follow-up and patient statements & collections. Our logo is red and blue-ish, so make sure that whatever other elements are used will match appropriately. Our current business card design has a too small font size. I'd like to project an image that shows we are modern & reliable. On a side note, I'm planning on using VUX for printing these cards.

Target Market(s)

Office managers, physicians, therapists

Industry/Entity Type

Printing

Requirements
Must have
• Logo
Name of Employee
Phone
Fax
E-mail
Website

```html
<!DOCTYPE html>
<html lang="en">
<head>
<meta charset="utf-8">
<title>Lorrimer Tallbrook Services – Business Card</title>
<link rel="stylesheet" href="https://fonts.googleapis.com/css2?family=Questrial&family=Montserrat:wght@600;700&display=swap">
<style>
  :root {
    --navy: #25206a;
    --navy-deep: #1c1858;
    --crimson: #a31d24;
    --crimson-deep: #8f161c;
    --paper: #efeff0;
    --backdrop: #d4d4d6;
    --ink-white: #ffffff;
  }
  * { margin: 0; padding: 0; box-sizing: border-box; }
  html, body {
    width: 1200px; height: 900px; overflow: hidden;
    background: var(--backdrop);
    font-family: "Questrial", "Century Gothic", sans-serif;
  }
  .sheet {
    width: 1200px; height: 900px;
    display: flex; flex-direction: column;
    align-items: center; justify-content: center; gap: 40px;
  }
  .card {
    width: 700px; height: 400px;
    box-shadow: 0 6px 18px rgba(0,0,0,.18);
    overflow: hidden;
  }
  /* back side */
  .card--back {
    background: linear-gradient(160deg, var(--navy) 0%, var(--navy-deep) 100%);
    display: flex; align-items: center; justify-content: center;
  }
  .brand {
    display: flex; align-items: center; gap: 14px;
    font-family: "Questrial", "Century Gothic", sans-serif;
    letter-spacing: 3px; text-transform: uppercase;
    white-space: nowrap;
  }
  .brand__mark { width: 18px; height: 18px; }
  .card--back .brand { color: var(--ink-white); font-size: 38px; }
  .card--back .brand__mark { background: var(--crimson); }
  /* front side */
  .card--front { display: flex; flex-direction: column; }
  .front__header {
    height: 112px;
    background: linear-gradient(100deg, var(--navy-deep) 0%, var(--navy) 100%);
    display: flex; align-items: flex-end; justify-content: center;
    padding-bottom: 22px;
    color: var(--ink-white);
  }
  .person__name {
    font-family: "Montserrat", sans-serif; font-weight: 700;
    font-size: 22px; letter-spacing: .5px;
  }
  .person__role { font-size: 18px; margin-left: 8px; }
  .front__logo {
    flex: 1; background: var(--paper);
    display: flex; align-items: center; justify-content: center;
  }
  .front__logo .brand { color: var(--navy); font-size: 40px; }
  .front__logo .brand__mark { background: var(--crimson); }
  .front__contact {
    height: 138px;
    background: linear-gradient(100deg, var(--crimson) 0%, var(--crimson-deep) 100%);
    color: var(--ink-white);
    display: flex; flex-direction: column; align-items: center; justify-content: center;
    gap: 5px; font-size: 17px; text-align: center;
  }
  .contact__label { font-family: "Montserrat", sans-serif; font-weight: 700; }
</style>
</head>
<body>
<main class="sheet">
  <section class="card card--back" aria-label="Card back">
    <div class="brand">
      <span class="brand__name">Lorrimer Tallbrook</span>
      <span class="brand__mark"></span>
    </div>
  </section>

  <section class="card card--front" aria-label="Card front">
    <header class="front__header">
      <span class="person__name">MARCUS HALE</span>
      <span class="person__role">/ Manager</span>
    </header>
    <div class="front__logo">
      <div class="brand">
        <span class="brand__name">Lorrimer Tallbrook</span>
        <span class="brand__mark"></span>
      </div>
    </div>
    <footer class="front__contact">
      <p>2187 NW Coral Bend Road, Harbor Vale, FL 34911 · <span class="contact__label">T:</span> 866 555 0142</p>
      <p><span class="contact__label">F:</span> 866 555 0187 · <span class="contact__label">E:</span> info@lorrimertallbrook.net</p>
      <p><span class="contact__label">W:</span> www.lorrimertallbrook.net</p>
    </footer>
  </section>
</main>
</body>
</html>
```